依頼詳細
袋のデザインと箱のデザインを希望します。
主に40代~60代の主婦層をターゲットに考えています。進物に使えるシンプルだけど高級感のあるイメージ。
因みに、『澄楓』の名前は毛筆で書かれた物で決定しています。
記載項目

サイズ:幅12.5mm×長さ16mm雲竜柄の白い袋を考えています。
栗入り、黒豆入り、あんず入り、ノーマルの4種類で統一感のあるもの。

紙箱(5個・10個・15個入りで同一デザイン)
サイズ:幅220mm×長さ310mm×高さ65mm(10個入り)
紙質:特に無し

希望イメージ
シンプル 複雑
単色 カラフル
暗い 明るい
日常 高級
遊び心 厳粛
未来的 伝統的
女性的 男性的
希望する色
白・黒・オレンジ・紫など
納品ファイル
• 高解像度JPG (.jpg)
• イラストレーター形式 (.ai)
補足説明
同じ大きさで、数種類のどら焼きがあるので、詰合せた時の統一感が出る様にお願いします。
今後も、種類を増やす予定。
この度、パッケージデザインご提案頂きありがとう御座います。

幾つか『澄楓』をsumikazeと表記されてるデザインがありましたので訂正をさせて頂きます。
『澄楓』≒sumika(すみか)です。よろしくお願いいたします。

澄楓の『信』は他界した先代社長から一字取りました。その志を継ぎ、本物を追及しながらも敷居を低くし、『少し贅沢なお菓子』を目指しています。『樂』にはお菓子を食べるシチュエーションを思い浮かべ、その場の雰囲気や人の心など、思わず笑顔になってしまうような空間を作りたいと思ってつけた名前です。

皆様、よろしくお願い致します。
沢山のデザインありがとうございます。

デザインの内容についてお願いがありますので追記致します。

弊社の会社のHPを見て頂いたランサー様の中に弊社の梅のロゴやたかむら製菓舗の名前をデザインに組み込まれてる方がおられますが、今回は弊社本体とはブランドイメージを分けて考えたいと思いますので、あくまで『澄楓』のイメージでロゴないし、デザインの制作をお願いいたします。
■ 選んだ理由

澄楓のブランドイメージを理解して頂き、こちらの細かい修正依頼にも、素早く丁寧に対応して頂きました。

今後もお世話になりたいランサー様に出会う事が出き感謝いたします。

■ 提案者全員のお礼・コメント

この度は、多くのデザインを提案して頂きありがとうございました。
皆さんレベルの高いデザインで選定には時間を要し非常に迷いました。

また、次の機会にも利用したいと思います。

有難うございました。

```html
<!DOCTYPE html>
<html lang="ja">
<head>
<meta charset="utf-8">
<title>澄楓 パッケージデザイン</title>
<link rel="stylesheet" href="https://fonts.googleapis.com/css2?family=Noto+Serif+JP:wght@500&family=Yuji+Boku&display=swap">
<style>
  :root {
    --paper: #ffffff;
    --ink: #050505;
    --circle-grey: #4b4b4d;
    --brush-lavender: #a9a3bd;
    --seal-red: #c63a22;
    --seal-text: #f3e3d6;
  }
  html, body {
    margin: 0;
    padding: 0;
    width: 880px;
    height: 1200px;
    overflow: hidden;
    background: var(--paper);
  }
  .package {
    position: relative;
    width: 880px;
    height: 1200px;
  }
  .package-art {
    position: absolute;
    inset: 0;
    display: block;
  }
  .ground { fill: var(--ink); }
  .ring, .disc { fill: var(--circle-grey); }
  .seal {
    position: absolute;
    left: 419px;
    top: 161px;
    width: 44px;
    height: 123px;
    background: var(--seal-red);
    display: flex;
    align-items: center;
    justify-content: center;
  }
  .seal-text {
    writing-mode: vertical-rl;
    font-family: "Noto Serif JP", serif;
    font-weight: 500;
    font-size: 22px;
    letter-spacing: 3px;
    color: var(--seal-text);
    margin: 0;
  }
  .brand-name {
    position: absolute;
    left: 270px;
    top: 300px;
    width: 380px;
    margin: 0;
    display: flex;
    flex-direction: column;
    align-items: center;
    font-family: "Yuji Boku", serif;
    font-weight: 400;
    font-size: 300px;
    line-height: 1;
    color: var(--brush-lavender);
  }
  .brand-char { display: block; }
  .brand-char + .brand-char { margin-top: -10px; margin-left: 40px; }
</style>
</head>
<body>
  <main class="package">
    <svg class="package-art" width="880" height="1200" viewBox="0 0 880 1200" aria-hidden="true">
      <defs>
        <clipPath id="panel-clip">
          <rect x="53" y="53" width="777" height="1083"/>
        </clipPath>
      </defs>
      <rect class="ground" x="53" y="53" width="777" height="1083"/>
      <g clip-path="url(#panel-clip)">
        <path class="ring" fill-rule="evenodd"
              d="M117 149 a182 182 0 1 0 0.1 0 Z M117 208 a123 123 0 1 1 -0.1 0 Z"/>
        <circle class="disc" cx="680" cy="967" r="152"/>
      </g>
    </svg>
    <div class="seal"><p class="seal-text">山里菓子</p></div>
    <h1 class="brand-name"><span class="brand-char">澄</span><span class="brand-char">楓</span></h1>
  </main>
</body>
</html>
```